2 Funky Pages + EASY stock logo = Construction Website

We would like a funky new website - Just 2 pages - to promote our project management company. A logo is also needed, but we'll provide a stock image which just needs a colour change a text added.

Here are the instructions:

"Fair Tally Homes"

#logo
The one I'd like is attached. Please change font and positioning of text though.

Tagline is "Don't be normal - Be clever"

#Colour combo
756897 Wood Veneer
D5D6D2 sand dollar
353C3F charcoal
962715 brick red

#Home - Page 1

Our cost-price home build service will save you thousands.
No, seriously - Here's how we do it (button)

- Pay what the home building companies do.
- FTH will manage the entire project.
- Use Keystonecraft Guaranteed builders and materials.
- Tender for the best industry rates.
- Get a full budget calculated for the build.
- Avoid inflated 'Fixed-price' builds.
See how it works (button)

Contact Us: 0800 615 278
enquire - Name, Phone, email, comment - SEND

#How it works - Page 2

Traditional fixed price contracts are popular because it means that any risk of unexpected problems is carried by the home builder, but the builder will generally load the price about 10 times above the actual risk carried.

It's like an over-priced insurance policy, on steroids.

Clever people do things differently.

Here's how a cost-price build works...

1) Tell us what you want to build. Dream home, townhouse, investment property, whatever.

2) We'll put a design together for you, or you can choose from a bunch of plans we've already got.

3) We'll give you a conservative price estimate.

4) We finish tweaking your plans, then send them out to our network of more than 200 builders, subcontractors and tradesmen.

5) We collect the quotes, pick the best prices, and finalise your budget. Now you buy us beer, cause you've finally realised how much you're saving.

6) Tell your friends how awesome we are, while we lodge your building consent application with Council.

7) We coordinate the builders and subbies (look, you're already speaking trade-talk) from start to finish. You pay the cost price on their work each month.

We're happy to talk numbers and give you an estimate.

Contact Us: 0800 615 278

Reason: I have seen some great design elements, but need them to come together in one site design. Also, there appears to be less attention paid to the second page design ('how it works') than is necessary... There is no viable contender there yet, compared with the great home page submissions. I've also added some further info to the brief, and note that many submissions have ignored the colour combo I've requested.

Industry/Entity Type

Construction

Number of Pages Required

2 page

Requirements
Must have
• Keystonecrafter logo (small)
• Colour combo described in brief.
Nice to have
• I've attached a stock image I like, but it's certainly not essential. I do like images with clear backgrounds though - they tend to produce a crisp looking site.
• There is a wider image similar to this, available on Pixel Vault, but Sketch Hive won't let me attach it.
Should not have
• Photos of cheesy American faces.

```html
<!DOCTYPE html>
<html lang="en">
<head>
<meta charset="utf-8">
<title>Fair Tally Homes</title>
<link rel="stylesheet" href="https://fonts.googleapis.com/css2?family=Kaushan+Script&family=Courgette&family=Lato:wght@400;700&family=Exo+2:wght@500;600&display=swap">
<style>
:root{
  --brick:#962715;
  --charcoal:#353c3f;
  --veneer:#756897;
  --sand:#d5d6d2;
  --footer:#23272f;
  --panel:#f3f3f3;
  --line:#e2e2e2;
  --text:#555;
  --white:#fff;
}
*{box-sizing:border-box;margin:0;padding:0}
html,body{width:881px;height:1200px;overflow:hidden;background:var(--white);font-family:"Lato",sans-serif}
.page{position:relative;width:881px;height:1200px}
.abs{position:absolute}

/* header */
.site-header{position:absolute;left:0;top:0;width:881px;height:75px;background:var(--white)}
.brand-mark{left:116px;top:22px;width:30px;height:30px;background:var(--brick)}
.brand-name{left:158px;top:22px;font-family:"Courgette",cursive;font-size:22px;line-height:30px;color:var(--brick);white-space:nowrap}
.header-phone{left:508px;top:31px;display:flex;align-items:center;gap:8px;font-family:"Exo 2",sans-serif;font-weight:600;font-size:14px;color:var(--charcoal);letter-spacing:.5px}
.header-cta{left:645px;top:29px;width:121px;height:23px;border:1px solid var(--brick);color:var(--brick);font-family:"Courgette",cursive;font-size:10px;display:flex;align-items:center;justify-content:center;gap:6px}

/* hero */
.hero{position:absolute;left:0;top:75px;width:881px;height:298px;background:linear-gradient(120deg,#a79f97 0%,#8c93a3 35%,#a9b0bd 65%,#c9cbd1 100%)}
.hero-title{position:absolute;left:0;top:104px;width:881px;text-align:center;font-family:"Kaushan Script",cursive;font-weight:400;font-size:26px;line-height:35px;color:var(--white)}
.hero-cta{position:absolute;left:326px;top:186px;width:205px;height:29px;background:var(--brick);color:var(--white);font-family:"Courgette",cursive;font-size:11px;display:flex;align-items:center;justify-content:center}
.hero-arrow{position:absolute;top:128px}

/* features */
.features{position:absolute;left:0;top:373px;width:881px;height:412px}
.features-aside{position:absolute;left:0;top:0;width:375px;height:412px;background:var(--panel)}
.feature-item{position:absolute;left:114px;width:261px;background:var(--white);border:1px solid var(--line);font-family:"Courgette",cursive;font-size:12px;line-height:14px;color:#666;padding:0 17px;display:flex;align-items:center}
.feature-item.is-active{background:var(--brick);border-color:var(--brick);color:var(--white);padding-left:23px}
.feature-item.is-active::after{content:"";position:absolute;right:-1px;top:50%;margin-top:-8px;border:8px solid transparent;border-right-color:var(--white)}
.feature-heading{position:absolute;left:420px;top:104px;width:360px;text-align:center;font-family:"Kaushan Script",cursive;font-weight:400;font-size:25px;line-height:29px;color:var(--brick)}
.feature-copy{position:absolute;left:420px;top:186px;width:360px;text-align:center;font-size:12px;line-height:14px;color:var(--text);letter-spacing:.3px}
.feature-cta{position:absolute;left:523px;top:259px;width:129px;height:23px;background:var(--brick);color:var(--white);font-family:"Exo 2",sans-serif;font-weight:500;font-size:12px;display:flex;align-items:center;justify-content:center;gap:5px}

/* footer */
.site-footer{position:absolute;left:0;top:785px;width:881px;height:415px;background:linear-gradient(180deg,#22262e 0%,#262b35 60%,#2c2c36 100%);color:var(--white)}
.footer-title{position:absolute;font-family:"Courgette",cursive;font-size:16px;color:var(--white)}
.footer-rule{position:absolute;width:36px;height:2px;background:var(--white)}
.field{position:absolute;left:114px;width:228px;border:1px solid #c9cbd0;font-size:9.5px;font-style:italic;color:#c4c6cb;padding:5px 7px}
.send-btn{position:absolute;left:115px;top:278px;width:132px;height:23px;background:var(--brick);font-family:"Courgette",cursive;font-size:11px;display:flex;align-items:center;justify-content:center;gap:7px}
.divider{position:absolute;left:440px;top:37px;width:1px;height:268px;background:#4a4e57}
.contact-name{position:absolute;left:552px;top:94px;font-family:"Courgette",cursive;font-size:13px}
.contact-address{position:absolute;left:552px;top:115px;font-size:11px;line-height:13px;color:#dfe0e3}
.contact-phone{position:absolute;left:556px;top:165px;font-family:"Exo 2",sans-serif;font-weight:600;font-size:15px;letter-spacing:1px}
.contact-email{position:absolute;left:556px;top:207px;font-size:11px;color:#e6e7ea}
.social{position:absolute;top:263px;width:19px;height:19px;background:#6a6d73}
.social.is-active{background:#3ca6dc}
.footer-line{position:absolute;left:98px;top:350px;width:687px;height:1px;background:#5a5e66}
.to-top{position:absolute;left:432px;top:341px;width:19px;height:19px;border:1px solid #7b7f87;border-radius:50%;background:var(--footer)}
.copyright{position:absolute;left:0;top:378px;width:881px;text-align:center;font-size:11px;color:#c9cbd0}
</style>
</head>
<body>
<div class="page">

  <header class="site-header">
    <div class="abs brand-mark"></div>
    <div class="abs brand-name">Fair Tally Homes</div>
    <div class="abs header-phone">
      <svg width="16" height="16" viewBox="0 0 24 24" fill="none" stroke="#962715" stroke-width="2"><path d="M5 3h4l2 5-3 2a11 11 0 0 0 6 6l2-3 5 2v4a2 2 0 0 1-2 2A17 17 0 0 1 3 5a2 2 0 0 1 2-2z"/><path d="M15 3a6 6 0 0 1 6 6M15 7a2 2 0 0 1 2 2"/></svg>
      0800 615 278
    </div>
    <div class="abs header-cta">See How it Works
      <svg width="8" height="8" viewBox="0 0 10 10"><circle cx="5" cy="5" r="4" fill="none" stroke="#962715" stroke-width="1.5"/><path d="M4 3l2 2-2 2" stroke="#962715" fill="none"/></svg>
    </div>
  </header>

  <section class="hero" role="img" aria-label="Construction workers building a timber house frame over architectural blueprints">
    <h1 class="hero-title">Our Cost-Price Home Build Service<br>Will Save You Thousands.</h1>
    <div class="hero-cta">No, seriously - Here's how we do it</div>
    <svg class="hero-arrow" style="left:28px" width="24" height="42" viewBox="0 0 24 42"><path d="M22 1L2 21l20 20" fill="none" stroke="#fff" stroke-width="1.6"/></svg>
    <svg class="hero-arrow" style="left:829px" width="24" height="42" viewBox="0 0 24 42"><path d="M2 1l20 20L2 41" fill="none" stroke="#fff" stroke-width="1.6"/></svg>
  </section>

  <section class="features">
    <div class="features-aside"></div>
    <div class="feature-item" style="top:41px;height:50px">Use Keystonecraft Guaranteed Builders<br>and materials</div>
    <div class="feature-item is-active" style="top:100px;height:50px">Pay what the Home Building<br>Companies do</div>
    <div class="feature-item" style="top:159px;height:49px">FTH will Manage The Entire Project</div>
    <div class="feature-item" style="top:218px;height:49px">Tender for the Best Industry Rate</div>
    <div class="feature-item" style="top:276px;height:41px">Get a Full Budget Calculated for<br>the Build</div>
    <div class="feature-item" style="top:327px;height:41px">Avoid Inflated 'Fixed-Price' Builds</div>

    <h2 class="feature-heading">Pay what the Home Building<br>Companies do</h2>
    <p class="feature-copy">Lorem Ipsum is simply dummy text of the printing and<br>typesetting industry. Lorem Ipsum has been<br>the industry's standard dummy text ever since</p>
    <div class="feature-cta">See how it works
      <svg width="8" height="8" viewBox="0 0 10 10"><circle cx="5" cy="5" r="4" fill="none" stroke="#fff" stroke-width="1.5"/><path d="M4 3l2 2-2 2" stroke="#fff" fill="none"/></svg>
    </div>
  </section>

  <footer class="site-footer">
    <div class="footer-title" style="left:114px;top:37px">Get in Touch</div>
    <div class="footer-rule" style="left:117px;top:66px"></div>
    <div class="field" style="top:99px;height:24px">Enter your Name</div>
    <div class="field" style="top:134px;height:24px">Phone Number</div>
    <div class="field" style="top:169px;height:24px">Email</div>
    <div class="field" style="top:204px;height:58px">Comment</div>
    <div class="send-btn">
      <svg width="10" height="10" viewBox="0 0 10 10"><path d="M10 0L0 4l4 1 1 4z" fill="#fff"/></svg>
      Send Your Enquire
    </div>

    <div class="divider"></div>

    <div class="footer-title" style="left:521px;top:38px">Contact Info</div>
    <div class="footer-rule" style="left:523px;top:66px"></div>
    <svg class="abs" style="left:522px;top:96px" width="11" height="15" viewBox="0 0 12 16"><path d="M6 0a6 6 0 0 0-6 6c0 4 6 10 6 10s6-6 6-10a6 6 0 0 0-6-6z" fill="#fff"/><circle cx="6" cy="6" r="2.2" fill="#23272f"/></svg>
    <div class="contact-name">Fair Tally Homes</div>
    <div class="contact-address">96 Lorem Ipsum, giving information<br>origins,&nbsp; as a random Lipsum (8645)</div>
    <svg class="abs" style="left:518px;top:165px" width="17" height="17" viewBox="0 0 24 24" fill="none" stroke="#fff" stroke-width="1.8"><path d="M5 3h4l2 5-3 2a11 11 0 0 0 6 6l2-3 5 2v4a2 2 0 0 1-2 2A17 17 0 0 1 3 5a2 2 0 0 1 2-2z"/><path d="M15 3a6 6 0 0 1 6 6M15 7a2 2 0 0 1 2 2"/></svg>
    <div class="contact-phone">0800 615 278</div>
    <svg class="abs" style="left:522px;top:208px" width="14" height="10" viewBox="0 0 14 10"><rect width="14" height="10" rx="1" fill="#fff"/><path d="M0 1l7 5 7-5" stroke="#23272f" fill="none"/></svg>
    <div class="contact-email">info@fairtallyhomes.com</div>
    <div class="social" style="left:521px"></div>
    <div class="social is-active" style="left:546px"></div>
    <div class="social" style="left:571px"></div>

    <div class="footer-line"></div>
    <div class="to-top">
      <svg width="17" height="17" viewBox="0 0 17 17"><path d="M5 10l3.5-3.5L12 10" fill="none" stroke="#9a9ea6" stroke-width="1.2"/></svg>
    </div>
    <div class="copyright">© Copyright 2016 Fair Tally Homes.</div>
  </footer>

</div>
</body>
</html>
```